Very Simple changes to a flyer

We just need to adjust this premade flyer slightly. Where it says Holvista to instead say corvana. Keep the Logo (1/2snowflake1/2sun) before the word, just change Holvista to corvana. There is 1 Holvista in the heading, and 1 in the bullet points. Make the corvana all orange. Make the corvana look like the uploaded lower case corvana text graphic. Then in the bottom middle of the flyer where the Holvista SLEEP SYSTEM logo is, KEEP that just make that a little smaller, so you can write above the word: corvana (in orange same as heading with out the logo, just the word corvana. Because the logo is already below) Then below that word corvana and above the Holvista logo write SUMMER COMFORTER (in black). So it will say Corvana SUMMER COMFORTER, above the Holvista SLEEP SYSTEMS.
Thank you
I need to choose a 2nd place entry, is anyone available right now. I would need the source files uploaded right away. Please do not commit if you are not able to do the work now. Please let me know if your are available.
Thank you

```html
<!DOCTYPE html>
<html lang="en">
<head>
<meta charset="utf-8">
<title>Corvana Premium Down Comforter Flyer</title>
<link href="https://fonts.googleapis.com/css2?family=Montserrat:wght@400;500;600;700&display=swap" rel="stylesheet">
<style>
  :root {
    --brand-blue: #1b75c0;
    --brand-orange: #f6921e;
    --ink: #1c1c1c;
    --paper: #ffffff;
    --stage: #e9e6e1;
    --photo-light: #f7f4ef;
    --photo-mid: #e6dfd6;
  }
  * { box-sizing: border-box; margin: 0; padding: 0; }
  html, body { width: 1200px; height: 900px; overflow: hidden; background: var(--stage); }
  body { font-family: "Montserrat", Arial, sans-serif; position: relative; }

  .flyer {
    position: absolute; left: 20px; top: 67px;
    width: 1160px; height: 766px;
    background: var(--paper); overflow: hidden;
  }
  .flyer-shapes { position: absolute; inset: 0; }

  .headline {
    position: absolute; left: 24px; top: 26px;
    color: var(--paper); font-weight: 400; font-size: 45px; line-height: 48px; letter-spacing: 0.5px;
  }
  .headline strong { font-weight: 700; }
  .brand-word { color: var(--brand-orange); font-weight: 500; }
  .brand-dot {
    display: inline-block; width: 0.55em; height: 0.55em; border-radius: 50%;
    background: var(--brand-orange); margin-right: 0.2em; vertical-align: 0.05em;
  }

  .lead {
    position: absolute; left: 26px; top: 134px; width: 590px;
    color: var(--paper); font-size: 20px; line-height: 28px;
  }
  .lead strong { font-weight: 700; }

  .new-label {
    position: absolute; left: 26px; top: 228px; width: 180px;
    border-top: 1px solid rgba(255,255,255,0.45); border-bottom: 1px solid rgba(255,255,255,0.45);
    color: var(--brand-orange); font-size: 19px; font-weight: 500; padding: 2px 0 0;
  }

  .feature-list {
    position: absolute; left: 26px; top: 272px; width: 545px; list-style: none;
    color: var(--paper); font-size: 15px; line-height: 19px;
  }
  .feature-list li { position: relative; padding-left: 24px; margin-bottom: 8px; }
  .feature-list li::before {
    content: ""; position: absolute; left: 2px; top: 4px; width: 11px; height: 11px;
    border-radius: 50%; background: var(--brand-orange);
  }
  .feature-list strong { font-weight: 700; }

  .seasons-title {
    position: absolute; left: 28px; top: 548px;
    font-size: 24px; font-weight: 400; color: var(--ink);
  }
  .season-equation { position: absolute; left: 134px; top: 596px; }

  .layer-card {
    position: absolute; top: 636px; width: 90px; height: 104px;
    background: var(--brand-blue); border-radius: 5px; padding: 18px 4px 18px;
  }
  .layer-card .cap, .layer-card .season {
    position: absolute; left: 0; right: 0; text-align: center;
    color: var(--paper); font-size: 11px; font-weight: 600;
  }
  .layer-card .cap { top: 3px; }
  .layer-card .season { bottom: 3px; }
  .layer-card .swatch {
    width: 100%; height: 100%;
    background: linear-gradient(160deg, #f4f4f2, #d7d7d3);
  }
  .card-one { left: 23px; }
  .card-two { left: 148px; }
  .card-three { left: 272px; }
  .operator { position: absolute; top: 662px; font-size: 32px; color: var(--ink); }
  .op-plus { left: 121px; }
  .op-equals { left: 246px; }

  .product-mark { position: absolute; left: 384px; top: 588px; }
  .product-mark .mark-name {
    color: var(--brand-orange); font-size: 56px; font-weight: 500; line-height: 60px;
  }
  .product-mark .mark-dot {
    display: inline-block; width: 28px; height: 28px; border-radius: 50%;
    background: var(--brand-orange); margin-right: 10px; vertical-align: 2px;
  }
  .product-mark .mark-sub {
    margin-left: 150px; font-size: 14px; color: var(--ink); letter-spacing: 0.3px;
  }

  .size-list { position: absolute; left: 406px; top: 685px; list-style: none; font-size: 12px; font-weight: 500; color: var(--ink); line-height: 18px; }
  .size-list li::before {
    content: ""; display: inline-block; width: 9px; height: 9px; border: 1px solid var(--ink);
    margin-right: 8px; vertical-align: -1px;
  }
</style>
</head>
<body>
<main class="flyer">
  <svg class="flyer-shapes" width="1160" height="766" viewBox="0 0 1160 766">
    <defs>
      <radialGradient id="bedding" cx="0.55" cy="0.5" r="0.6">
        <stop offset="0" stop-color="var(--photo-light)"/>
        <stop offset="1" stop-color="var(--photo-mid)"/>
      </radialGradient>
      <path id="badge-arc" d="M930,660 A78,78 0 0 0 1080,640"/>
    </defs>
    <path d="M0,0 H1160 V640 L860,560 Q420,600 0,492 Z" fill="var(--brand-orange)"/>
    <path d="M0,0 H1160 V600 L860,530 Q420,565 0,470 Z" fill="var(--brand-blue)"/>
    <circle cx="906" cy="345" r="300" fill="var(--brand-orange)"/>
    <circle cx="906" cy="345" r="278" fill="url(#bedding)" role="img" aria-label="Photo: woman resting on a white down comforter and pillow"/>
    <circle cx="1003" cy="633" r="104" fill="var(--brand-orange)"/>
    <circle cx="1003" cy="633" r="92" fill="var(--paper)"/>
    <circle cx="1003" cy="618" r="64" fill="#ecebe6" role="img" aria-label="Photo: close-up of the comforter corner with snap fastener"/>
    <text font-family="Montserrat, Arial, sans-serif" font-size="19" font-weight="500" fill="var(--brand-blue)">
      <textPath href="#badge-arc" startOffset="4%">Duo Clasp System</textPath>
    </text>
  </svg>

  <h1 class="headline">
    <strong>Introducing</strong> The <span class="brand-word"><span class="brand-dot"></span>corvana</span><br>
    Premium Down Comforter
  </h1>

  <p class="lead">The <strong>perfect</strong> summer sleeper on its own is also capable of snapping to a second <span class="brand-word"><span class="brand-dot"></span>corvana</span> for winter warmth.</p>

  <div class="new-label">NEW</div>
  <ul class="feature-list">
    <li>Patent Pending <strong>Duo Clasp System</strong> designed for seasonal versatility.</li>
    <li>Purchase a second <span class="brand-word">corvana</span> for dual-layer winter warmth.</li>
    <li>A twin can snap over the left or right side of a king to accommodate both hot and cold sleepers simultaneously.</li>
    <li>Filled with 600+ <strong>hypo-allergenic</strong> white Euro Down Clusters.</li>
    <li>Sewn thru construction.</li>
    <li>300 Thread Count Down-Proof, <strong>Soft</strong> and Luxurious 100% cambric cotton.</li>
  </ul>

  <h2 class="seasons-title">Because seasons change...</h2>
  <svg class="season-equation" width="120" height="24" viewBox="0 0 120 24" aria-label="summer plus summer equals winter">
    <g fill="none" stroke="#888" stroke-width="2">
      <circle cx="12" cy="12" r="6"/>
      <path d="M30,12 h10 M35,7 v10"/>
      <circle cx="58" cy="12" r="6"/>
      <path d="M76,9 h10 M76,15 h10"/>
      <path d="M104,3 v18 M96,7 l16,10 M96,17 l16,-10"/>
    </g>
  </svg>

  <div class="layer-card card-one"><span class="cap">Single Layer</span><div class="swatch" role="img" aria-label="Single summer layer"></div><span class="season">Summer</span></div>
  <span class="operator op-plus">+</span>
  <div class="layer-card card-two"><span class="cap">Single Layer</span><div class="swatch" role="img" aria-label="Single summer layer"></div><span class="season">Summer</span></div>
  <span class="operator op-equals">=</span>
  <div class="layer-card card-three"><span class="cap">Dual Layers</span><div class="swatch" role="img" aria-label="Two layers snapped together"></div><span class="season">Winter</span></div>

  <div class="product-mark">
    <div class="mark-name"><span class="mark-dot"></span>corvana</div>
    <div class="mark-sub">SUMMER COMFORTER</div>
  </div>

  <ul class="size-list">
    <li>Twin 63” x 94” California XL = 10.oz/Down</li>
    <li>Full/Queen 88” x 94” California XL = 14.oz/Down</li>
    <li>King 106” x 94” California XL = 17.oz/Down</li>
  </ul>
</main>
</body>
</html>
```